Electrical company business card design.

Hi, were an electrical company in Harrowfield New Zealand called Quarneth Ltd. We focus mainly on high end residential and commercial so the card would be targeted towards that.
The card will be for myself, i am the director of the company.
Name: Derek Olstow
Position: Director/electrician
Phone: 021 387 9415
Email: derek@quarneth.co.nz
Location: Harrowfield
As for colors the the blue color in the logo is preferred, i also don't mind a black background option.
Target Market(s)
High end residential and commercial
Industry/Entity Type
Electrician
Contact Information for Business Card
Name: Derek Olstow Position: Director/Electrician Phone: 021 387 9415, Email: derek@quarneth.co.nz, Location: Harrowfield

```html
<!DOCTYPE html>
<html lang="en">
<head>
<meta charset="utf-8">
<title>Quarneth Ltd – Business Card</title>
<link href="https://fonts.googleapis.com/css2?family=Montserrat:wght@400;500;600;700&display=swap" rel="stylesheet">
<style>
  :root {
    --page-bg: #2b2b2d;
    --card-bg: #1f1f21;
    --brand-grey: #5b5e63;
    --tagline-grey: #55585c;
    --text-white: #f4f4f4;
    --text-soft: #d9d9d9;
    --accent-blue: #1f6fc4;
    --sheen-dark: #0c0c0d;
    --sheen-light: #3a3a3e;
  }
  * { margin: 0; padding: 0; box-sizing: border-box; }
  html, body {
    width: 1200px; height: 874px; overflow: hidden;
    background: var(--page-bg);
    font-family: "Montserrat", sans-serif;
  }
  .canvas { position: relative; width: 1200px; height: 874px; }
  .card {
    position: absolute; left: 270px; width: 660px; height: 380px;
    background: var(--card-bg);
    border-radius: 22px;
    overflow: hidden;
    box-shadow: 0 14px 30px rgba(0,0,0,.45);
  }
  .card--front { top: 40px; }
  .card--back { top: 454px; }

  .brand-decoration {
    position: absolute; left: 0; top: 0; width: 660px; height: 380px; display: block;
  }

  .brand {
    position: absolute;
    display: flex; flex-direction: column; align-items: flex-start;
  }
  .card--front .brand { left: 44px; top: 150px; }
  .card--back .brand { left: 300px; top: 70px; }

  .brand-row { display: flex; align-items: center; gap: 10px; }
  .brand-name {
    font-weight: 600; font-size: 52px; letter-spacing: 1px;
    color: var(--brand-grey); line-height: 1;
  }
  .brand-square { width: 12px; height: 12px; background: var(--accent-blue); }
  .brand-tagline {
    margin-top: 8px;
    font-weight: 600; font-size: 15px; letter-spacing: 1.6px;
    color: var(--tagline-grey); text-transform: uppercase;
  }

  .contact-block { position: absolute; left: 330px; top: 192px; }
  .person-name { font-weight: 700; font-size: 26px; color: var(--text-white); line-height: 1.1; }
  .person-role { font-weight: 600; font-size: 15px; color: var(--accent-blue); margin-top: 2px; }
  .contact-list { list-style: none; margin-top: 16px; }
  .contact-item {
    display: flex; align-items: center; gap: 12px;
    font-size: 15px; font-weight: 500; color: var(--text-soft);
    height: 27px;
  }
  .contact-item--location { font-weight: 600; color: var(--text-white); }
  .contact-icon { width: 15px; height: 15px; flex: none; fill: var(--accent-blue); }
</style>
</head>
<body>
<main class="canvas">

  <section class="card card--front" aria-label="Card front">
    <svg class="brand-decoration" role="img" aria-label="Large glossy brand mark decoration" viewBox="0 0 660 380">
      <defs>
        <radialGradient id="sheenFront" cx="0.72" cy="0.35" r="0.5">
          <stop offset="0" stop-color="var(--sheen-light)" stop-opacity=".45"/>
          <stop offset=".55" stop-color="var(--sheen-dark)" stop-opacity=".35"/>
          <stop offset="1" stop-color="var(--card-bg)" stop-opacity="0"/>
        </radialGradient>
      </defs>
      <rect width="660" height="380" fill="url(#sheenFront)"/>
    </svg>
    <div class="brand">
      <div class="brand-row">
        <span class="brand-name">QUARNETH</span>
        <span class="brand-square"></span>
      </div>
      <span class="brand-tagline">Energy built to last</span>
    </div>
  </section>

  <section class="card card--back" aria-label="Card back">
    <svg class="brand-decoration" role="img" aria-label="Large glossy brand mark decoration" viewBox="0 0 660 380">
      <defs>
        <radialGradient id="sheenBack" cx="0.22" cy="0.45" r="0.45">
          <stop offset="0" stop-color="var(--sheen-light)" stop-opacity=".4"/>
          <stop offset=".55" stop-color="var(--sheen-dark)" stop-opacity=".35"/>
          <stop offset="1" stop-color="var(--card-bg)" stop-opacity="0"/>
        </radialGradient>
      </defs>
      <rect width="660" height="380" fill="url(#sheenBack)"/>
    </svg>

    <div class="brand">
      <div class="brand-row">
        <span class="brand-name">QUARNETH</span>
        <span class="brand-square"></span>
      </div>
      <span class="brand-tagline">Energy built to last</span>
    </div>

    <div class="contact-block">
      <h1 class="person-name">Derek Olstow</h1>
      <p class="person-role">Director/electrician</p>
      <ul class="contact-list">
        <li class="contact-item">
          <svg class="contact-icon" viewBox="0 0 24 24" aria-hidden="true"><path d="M6.6 10.8a15.1 15.1 0 0 0 6.6 6.6l2.2-2.2a1 1 0 0 1 1-.25 11.4 11.4 0 0 0 3.6.57 1 1 0 0 1 1 1V20a1 1 0 0 1-1 1A17 17 0 0 1 3 4a1 1 0 0 1 1-1h3.5a1 1 0 0 1 1 1c0 1.25.2 2.45.57 3.57a1 1 0 0 1-.25 1z"/></svg>
          021 387 9415
        </li>
        <li class="contact-item">
          <svg class="contact-icon" viewBox="0 0 24 24" aria-hidden="true"><path d="M2 5h20v14H2z"/><path d="M2 5l10 8 10-8" fill="none" stroke="var(--card-bg)" stroke-width="2"/></svg>
          derek@quarneth.co.nz
        </li>
        <li class="contact-item">
          <svg class="contact-icon" viewBox="0 0 24 24" aria-hidden="true"><circle cx="12" cy="12" r="10"/><path d="M2 12h20M12 2c3 3 3 17 0 20M12 2c-3 3-3 17 0 20" fill="none" stroke="var(--card-bg)" stroke-width="1.6"/></svg>
          www.quarneth.co.nz
        </li>
        <li class="contact-item contact-item--location">
          <svg class="contact-icon" viewBox="0 0 24 24" aria-hidden="true"><path d="M12 2a7 7 0 0 0-7 7c0 5 7 13 7 13s7-8 7-13a7 7 0 0 0-7-7zm0 9.5A2.5 2.5 0 1 1 12 6.5a2.5 2.5 0 0 1 0 5z"/></svg>
          Harrowfield
        </li>
      </ul>
    </div>
  </section>

</main>
</body>
</html>
```